Brightvale Advisory Inc. (Enterprise Resource Planning - All KRT)

I need a logo and business card design for an ERP consulting company based in Dallas, We specifically provide consulting services for implementing and maintaining KRT ERP systems, I would like to see all the colors be navy and white. White Card on one side with Navy print, and Navy card on the other side with White print. The design should communicate that we "Prevail" results by effort, skill and courage.

Target Market(s)

Meridian 400 companies that are implementing or maintaining an KRT ERP system. My specialty is Finance and Controlling

Industry/Entity Type

Business Consultant

Contact Information for Business Card

Dana Holbrook
President / CEO

2380 Wrenfield Lane
Prosper, Texas 75341

Tel: 214-583-0972
eMail: dana.holbrook@brightvaleadvisory.co
web: www.brightvaleadvisory.co

Logo Text

This needs to be a Graphic Design

Font styles to use
Sans Serif

Colors
0555a3
ffffff

Requirements
Must have
• two sided
• Front side - Navy card with white print
• name, title, telephone, email
• Back side - White card with navy print
• street address, web address,
• Slogan [Prevail ~ Effort, Skill, and Courage}
Nice to have
• Classic and Clean
Should not have
• typical IT stuff... we are a consulting service organization not an IT department.

```html
<!DOCTYPE html>
<html lang="en">
<head>
<meta charset="utf-8">
<title>Brightvale Advisory Inc. – Business Card</title>
<link rel="stylesheet" href="https://fonts.googleapis.com/css2?family=Source+Sans+3:wght@400;600&display=swap">
<style>
  :root {
    --navy: #0555a3;
    --paper: #f2f2f2;
    --ink: #1c1c1c;
    --stage: #000000;
    --white: #ffffff;
  }
  * { margin: 0; padding: 0; box-sizing: border-box; }
  html, body { width: 1200px; height: 900px; overflow: hidden; background: var(--stage); }
  body { position: relative; font-family: "Source Sans 3", "Myriad Pro", Arial, sans-serif; }

  .card { position: absolute; top: 200px; width: 310px; height: 502px; overflow: hidden; }

  .card-back {
    left: 265px; background: var(--paper); color: var(--ink);
    border-radius: 55px 0 55px 0;
  }
  .card-front {
    left: 641px; background: var(--navy); color: var(--white);
    border-radius: 50px 50px 0 50px;
  }

  .wordmark { position: absolute; display: flex; align-items: center; gap: 12px; }
  .wordmark-square { width: 30px; height: 30px; flex: none; }
  .wordmark-text {
    font-weight: 600; font-size: 25px; line-height: 1.05; letter-spacing: 0.6px;
    text-transform: uppercase; white-space: nowrap;
  }

  .card-back .wordmark { left: 34px; top: 54px; }
  .card-back .wordmark-square { background: var(--navy); }
  .card-back .wordmark-text { color: var(--navy); }

  .card-front .wordmark { left: 32px; top: 224px; }
  .card-front .wordmark-square { background: var(--white); }
  .card-front .wordmark-text { color: var(--white); }

  /* Front: name, title, phone, email */
  .person { position: absolute; left: 34px; top: 318px; }
  .person-name { font-weight: 600; font-size: 18.5px; line-height: 1; }
  .person-title { font-size: 14px; margin-top: 9px; line-height: 1; }

  .contact-list { list-style: none; margin-top: 18px; font-size: 13.6px; }
  .contact-list li { display: flex; align-items: center; gap: 6px; height: 19px; white-space: nowrap; }
  .contact-list svg { width: 11px; height: 11px; flex: none; }
  .card-front .contact-list svg { fill: var(--white); }
  .card-back .contact-list svg { fill: var(--navy); }

  /* Back: web, street address, slogan */
  .location { position: absolute; left: 26px; top: 340px; }
  .location .contact-list { margin-top: 0; }
  .address { font-size: 16px; line-height: 19px; margin-top: 9px; }
  .address span { display: block; }
  .address span + span { padding-left: 2px; }
  .slogan {
    margin-top: 22px; font-size: 14px; font-weight: 600; color: var(--navy);
    line-height: 1;
  }
</style>
</head>
<body>

<section class="card card-back" aria-label="Back side">
  <div class="wordmark">
    <span class="wordmark-square"></span>
    <span class="wordmark-text">Brightvale<br>Advisory Inc.</span>
  </div>

  <div class="location">
    <ul class="contact-list">
      <li>
        <svg viewBox="0 0 24 24" aria-hidden="true"><circle cx="12" cy="12" r="10"/></svg>
        www.brightvaleadvisory.co
      </li>
    </ul>
    <p class="address">
      <span>2380 Wrenfield Lane Prosper,</span>
      <span>Texas 75341</span>
    </p>
    <p class="slogan">Prevail ~ Effort, Skill, and Courage</p>
  </div>
</section>

<section class="card card-front" aria-label="Front side">
  <div class="wordmark">
    <span class="wordmark-square"></span>
    <span class="wordmark-text">Brightvale<br>Advisory Inc.</span>
  </div>

  <div class="person">
    <p class="person-name">Dana Holbrook</p>
    <p class="person-title">President / CEO</p>
    <ul class="contact-list">
      <li>
        <svg viewBox="0 0 24 24" aria-hidden="true"><path d="M6.6 10.8a15.1 15.1 0 0 0 6.6 6.6l2.2-2.2a1 1 0 0 1 1-.25 11.4 11.4 0 0 0 3.6.57 1 1 0 0 1 1 1V20a1 1 0 0 1-1 1A17 17 0 0 1 3 4a1 1 0 0 1 1-1h3.5a1 1 0 0 1 1 1c0 1.25.2 2.45.57 3.57a1 1 0 0 1-.25 1z"/></svg>
        214-583-0972
      </li>
      <li>
        <svg viewBox="0 0 24 24" aria-hidden="true"><path d="M2 5h20v2.2l-10 6.3L2 7.2z"/><path d="M2 9.6l10 6.3 10-6.3V19H2z"/></svg>
        dana.holbrook@brightvaleadvisory.co
      </li>
    </ul>
  </div>
</section>

</body>
</html>
```